Design a BOLD Ad Design for Fitness Club

We are fitness facility that is about to run our new "Bright Parent Reboot" program and we need a bold design created for an ad that will run on Instagram and Facebook.

The ad needs to be eye catching, easy to read and attractive so that someone stops scrolling and clicks to join.

The add needs to be sized to 1080 x 1080, include our logo and the text "Bright Parent Reboot" and "Starting September 23rd"

I have included an example photo, which is to be used as an example only of a design style that stands out to us, (colors, female photo style, etc)

I have also included our logo, which the yellow color can be changed for this design.

Thank you and we look forward to seeing your design.

```html
<!DOCTYPE html>
<html lang="en">
<head>
<meta charset="utf-8">
<title>Bright Parent Reboot – PulseForge</title>
<link href="https://fonts.googleapis.com/css2?family=Big+Shoulders+Stencil+Display:wght@800;900&family=Montserrat:wght@700&display=swap" rel="stylesheet">
<style>
  :root {
    --navy-deep: #050d2e;
    --navy: #0b1f5c;
    --blue-mid: #1f5fc0;
    --blue-bright: #3f9be6;
    --mist: #bfe6fb;
    --yellow: #f7d117;
    --ink: #111111;
    --white: #ffffff;
  }
  * { margin: 0; padding: 0; box-sizing: border-box; }
  html, body { width: 1200px; height: 1200px; overflow: hidden; background: var(--navy-deep); }
  .ad {
    position: relative;
    width: 1200px;
    height: 1200px;
    overflow: hidden;
    background:
      radial-gradient(ellipse 520px 300px at 300px 1010px, var(--mist) 0%, rgba(191,230,251,0.55) 30%, rgba(63,155,230,0.35) 60%, rgba(63,155,230,0) 100%),
      radial-gradient(ellipse 700px 520px at 260px 880px, var(--blue-bright) 0%, var(--blue-mid) 45%, rgba(31,95,192,0) 100%),
      radial-gradient(ellipse 900px 700px at 500px 300px, var(--navy) 0%, var(--navy-deep) 100%);
  }
  .headline {
    position: absolute;
    left: 72px;
    top: 58px;
    font-family: "Big Shoulders Stencil Display", "Stardos Stencil", sans-serif;
    font-weight: 900;
    color: var(--yellow);
    text-transform: uppercase;
    line-height: 1;
  }
  .headline span { display: block; letter-spacing: 4px; }
  .headline .line-1 { font-size: 118px; }
  .headline .line-2 { font-size: 152px; margin-top: 16px; }
  .headline .line-3 { font-size: 152px; margin-top: 16px; }
  .brand {
    position: absolute;
    left: 72px;
    top: 580px;
    font-family: "Montserrat", sans-serif;
  }
  .brand-name {
    font-weight: 700;
    font-size: 92px;
    letter-spacing: -2px;
    color: var(--white);
    line-height: 1;
  }
  .brand-tagline {
    margin-top: 22px;
    margin-left: 92px;
    font-weight: 700;
    font-size: 20px;
    letter-spacing: 3px;
    color: var(--yellow);
  }
  .date-band {
    position: absolute;
    left: 0;
    bottom: 0;
    width: 736px;
    height: 136px;
    background: var(--yellow);
    display: flex;
    align-items: center;
    padding-left: 58px;
  }
  .date-band p {
    font-family: "Big Shoulders Stencil Display", "Stardos Stencil", sans-serif;
    font-weight: 800;
    font-size: 60px;
    letter-spacing: 2px;
    color: var(--ink);
    text-transform: uppercase;
  }
  .date-band .suffix { text-transform: none; }
  .hero-photo {
    position: absolute;
    right: 0;
    top: 64px;
    width: 560px;
    height: 1136px;
    border-radius: 260px 260px 0 0;
    background: linear-gradient(180deg, #d8bd7e 0%, #c79a72 22%, #8a8d8f 45%, #7b7f82 70%, #1c1c1e 88%, #141416 100%);
  }
</style>
</head>
<body>
  <main class="ad">
    <h1 class="headline">
      <span class="line-1">Bright</span>
      <span class="line-2">Parent</span>
      <span class="line-3">Reboot</span>
    </h1>

    <div class="brand">
      <div class="brand-name">PulseForge</div>
      <div class="brand-tagline">PERSONAL GROUP TRAINING</div>
    </div>

    <div class="hero-photo" role="img" aria-label="Photo of a smiling athletic woman with long wavy blonde hair, wearing a grey tank top and black shorts, hands on hips"></div>

    <div class="date-band">
      <p>Starting September 23<span class="suffix">rd</span></p>
    </div>
  </main>
</body>
</html>
```